Business Card & Stationary for Jeweller | ||
Pearl Marquise Inc. | ||
Use same font as used in my logo | ||
Modern Professional Bright & Fun-filled |
Lorraine Whitcombe | ||
President & Principal Designer | ||
By Appointment | ||
lwhitcombe@pearlmarquise-example.ca | ||
www.pearlmarquise-example.ca | ||
Please add: Chatterbook Logo plus www.chatterbook-example.com/PearlMarquiseGems Chirpline Logo plus @RovingGemsmith NCF (National Crystalline Foundation) Logo Ethical Gemcraft Alliance Logo **I would like to incorporate a white background with black polka dots somehow on both the business card and stationary. I want glamour, trendy, feminine.** |
We customize each design experience to the clients requirements and bring our expertise and design tools to you! Complimentary Diamond Insurance for 12 months after purchase. Lifetime Manufacturing Warranty Free Lifetime Trade-Up Program Complimentary Champagne Delivery by Appointment Included |

```html
<!DOCTYPE html>
<html lang="en">
<head>
<meta charset="utf-8">
<title>Pearl Marquise Inc. — Business Card</title>
<link href="https://fonts.googleapis.com/css2?family=Cormorant+Garamond:wght@400;500&family=Open+Sans:wght@400;600&display=swap" rel="stylesheet">
<style>
  :root {
    --canvas: #d9d6d4;
    --frost-top: #f7f7f7;
    --frost-bottom: #e4e4e6;
    --silver-light: #f3f3f4;
    --silver-dark: #c9cacd;
    --pink: #f48fb4;
    --pink-deep: #e8609a;
    --white: #ffffff;
  }
  * { margin: 0; padding: 0; box-sizing: border-box; }
  html, body {
    width: 1200px;
    height: 768px;
    overflow: hidden;
    background: var(--canvas);
  }
  .canvas {
    width: 1200px;
    height: 768px;
    display: flex;
    align-items: center;
    justify-content: center;
  }
  .business-card {
    position: relative;
    width: 1000px;
    height: 560px;
    border-radius: 8px;
    overflow: hidden;
    background: linear-gradient(180deg, var(--frost-top) 0%, var(--frost-bottom) 100%);
    box-shadow: 0 10px 30px rgba(0,0,0,0.12);
  }
  .brand {
    position: absolute;
    left: 550px;
    top: 145px;
    transform: translate(-50%, -50%);
    display: flex;
    align-items: center;
    gap: 14px;
  }
  .brand-dot {
    width: 22px;
    height: 22px;
    border-radius: 50%;
    background: var(--pink);
  }
  .brand-name {
    font-family: "Cormorant Garamond", serif;
    font-weight: 500;
    font-size: 40px;
    color: var(--pink-deep);
    letter-spacing: 1px;
  }
  .info-band {
    position: absolute;
    left: 0;
    top: 285px;
    width: 100%;
    height: 180px;
    background: var(--pink);
  }
  .band-notch {
    position: absolute;
    left: 178px;
    top: 285px;
    width: 0;
    height: 0;
    border-left: 16px solid transparent;
    border-right: 16px solid transparent;
    border-top: 16px solid var(--frost-bottom);
  }
  .holder {
    position: absolute;
    left: 98px;
    top: 75px;
    color: var(--white);
  }
  .holder-name {
    font-family: "Cormorant Garamond", serif;
    font-weight: 400;
    font-size: 30px;
    letter-spacing: 1px;
  }
  .holder-title {
    font-family: "Open Sans", sans-serif;
    font-size: 17px;
    margin-top: 4px;
  }
  .band-divider {
    position: absolute;
    left: 435px;
    top: 30px;
    width: 2px;
    height: 125px;
    background: rgba(255,255,255,0.85);
  }
  .contact-list {
    position: absolute;
    left: 475px;
    top: 38px;
    list-style: none;
    font-family: "Open Sans", sans-serif;
    font-size: 17px;
    color: var(--white);
  }
  .contact-item {
    display: flex;
    align-items: center;
    gap: 14px;
    height: 36px;
  }
  .contact-icon {
    width: 22px;
    height: 22px;
    flex: none;
  }
  .silver-strip {
    position: absolute;
    left: 0;
    bottom: 0;
    width: 100%;
    height: 95px;
    background: linear-gradient(180deg, var(--silver-dark) 0%, var(--silver-light) 55%, var(--silver-dark) 100%);
  }
</style>
</head>
<body>
<main class="canvas">
  <article class="business-card">
    <div class="brand">
      <span class="brand-dot"></span>
      <span class="brand-name">Pearl Marquise</span>
    </div>

    <section class="info-band">
      <div class="holder">
        <p class="holder-name">Lorraine Whitcombe</p>
        <p class="holder-title">President &amp; Principal Designer</p>
      </div>
      <div class="band-divider"></div>
      <ul class="contact-list">
        <li class="contact-item">
          <svg class="contact-icon" viewBox="0 0 22 22" aria-hidden="true">
            <circle cx="11" cy="11" r="11" fill="#fff"/>
            <path d="M7 5.5c.6-.4 1.3-.2 1.6.4l1 2c.2.5.1 1-.3 1.3l-.8.6c.6 1.4 1.6 2.4 3 3l.6-.8c.3-.4.9-.5 1.3-.3l2 1c.6.3.8 1 .4 1.6l-.7 1c-.5.7-1.4 1-2.2.7-3.2-1.1-5.6-3.5-6.7-6.7-.3-.8 0-1.7.7-2.2z" fill="var(--pink)"/>
          </svg>
          <span>1-555-014-2271</span>
        </li>
        <li class="contact-item">
          <svg class="contact-icon" viewBox="0 0 22 22" aria-hidden="true">
            <circle cx="11" cy="11" r="11" fill="#fff"/>
            <rect x="7.5" y="4.5" width="7" height="13" rx="1.5" fill="var(--pink)"/>
            <rect x="8.7" y="6" width="4.6" height="8.5" fill="#fff"/>
            <circle cx="11" cy="16" r="0.8" fill="#fff"/>
          </svg>
          <span>1-555-014-2272</span>
        </li>
        <li class="contact-item">
          <svg class="contact-icon" viewBox="0 0 22 22" aria-hidden="true">
            <circle cx="11" cy="11" r="11" fill="#fff"/>
            <rect x="5" y="7" width="12" height="8.5" rx="1" fill="var(--pink)"/>
            <path d="M5.5 7.5l5.5 4.3 5.5-4.3" fill="none" stroke="#fff" stroke-width="1.2"/>
          </svg>
          <span>lwhitcombe@pearlmarquise-example.ca</span>
        </li>
      </ul>
    </section>
    <div class="band-notch"></div>

    <div class="silver-strip"></div>
  </article>
</main>
</body>
</html>
```